Eye Doctor Needs Updated Business Card

We need a standard US business card designed for an optometrist's practice. Our practice name is Halvorn Vision Center and attached you'll find our logos. We are located in a smaller community, we are a trusted source for eye care and designer eyewear. We have 2 different version of our logos, so both versions are attached. Our slogan is "Neighborly Service, Expert Eye Care". I'd like to see designs with one of our logos on the front with our contact info, and have the slogan on the back by itself. Final design should be professional looking, include the colors of our logo or colors that compliment the logo. We want it to look appropriate for a healthcare practice but also up-to-date, eye-catching, to have the normal contact info like address, phone #, email, but also possibly room for additional contact info such as facebook.
Updates

I just uploaded .eps files to use instead of the jpeg. Hope that helps!

So many great designs! We tending to like the darker blues that are used in our logo as the main blue color for the business cards. We also really like the use of a water-mark type appearance on either the front and/or back, or the embossed look as well looks nice. Thank you all for such great designs!

We're preferring the designs where white and the darker blue used in our logo are the primary colors on the front, but with a little green used as well. Again though, thanks for all the impressive designs so far!

Industry/Entity Type

Healthcare

```html
<!DOCTYPE html>
<html lang="en">
<head>
<meta charset="utf-8">
<title>Halvorn Vision Center – Business Card</title>
<link rel="stylesheet" href="https://fonts.googleapis.com/css2?family=Marcellus&family=Tinos&display=swap">
<style>
  :root {
    --page: #ffffff;
    --card: #ffffff;
    --card-edge: #c9c9c9;
    --brand-blue: #1f5f8a;
    --brand-green: #6aa86a;
    --ink: #3d3d3d;
    --ink-soft: #4a4a4a;
  }
  * { margin: 0; padding: 0; box-sizing: border-box; }
  html, body {
    width: 1026px; height: 1200px; overflow: hidden;
    background: var(--page);
  }
  .card {
    position: absolute; left: 47px; width: 868px; height: 532px;
    background: var(--card);
    border: 1.5px solid var(--card-edge);
  }
  .card--front { top: 60px; }
  .card--back { top: 640px; }

  .brand-mark {
    position: absolute; border-radius: 50%;
    background: var(--brand-green);
  }
  .brand-block {
    position: absolute; text-align: center; white-space: nowrap;
  }
  .brand-name {
    font-family: "Marcellus", serif; font-weight: 400;
    color: var(--brand-blue); line-height: 1.1;
  }
  .brand-name__sub { display: block; }

  /* front */
  .card--front .brand-mark { left: 148px; top: 149px; width: 135px; height: 135px; }
  .card--front .brand-block { left: 45px; width: 340px; top: 300px; }
  .card--front .brand-name { font-size: 40px; }
  .card--front .brand-name__sub { font-size: 24px; letter-spacing: 10px; margin-top: 2px; }
  .divider {
    position: absolute; left: 427px; top: 146px;
    width: 3px; height: 239px; background: var(--brand-blue);
  }
  .contact-list { position: absolute; left: 458px; top: 190px; list-style: none; }
  .contact-item {
    display: flex; align-items: center; gap: 8px; height: 56px;
    font-family: "Tinos", serif; font-size: 25px; color: var(--ink);
  }
  .contact-icon { width: 28px; height: 28px; flex: none; }
  .address {
    position: absolute; left: 0; right: 0; top: 482px; text-align: center;
    font-family: "Tinos", serif; font-size: 27px; color: var(--ink);
  }

  /* back */
  .card--back .brand-mark { left: 45px; top: 147px; width: 206px; height: 206px; }
  .card--back .brand-block { left: 283px; width: 540px; top: 180px; }
  .card--back .brand-name { font-size: 62px; }
  .card--back .brand-name__sub { font-size: 36px; letter-spacing: 16px; margin-top: 4px; }
  .slogan {
    margin-top: 22px;
    font-family: "Marcellus", serif; font-size: 27px; color: var(--ink-soft);
    letter-spacing: 0.5px;
  }
</style>
</head>
<body>
  <section class="card card--front">
    <div class="brand-mark"></div>
    <div class="brand-block">
      <div class="brand-name">Halvorn Vision<span class="brand-name__sub">Center</span></div>
    </div>
    <div class="divider"></div>
    <ul class="contact-list">
      <li class="contact-item">
        <svg class="contact-icon" viewBox="0 0 28 28" aria-hidden="true">
          <circle cx="14" cy="14" r="12.5" fill="none" stroke="#3d3d3d" stroke-width="1.5"/>
          <path d="M9.5 8.5 l2.5-1 1.8 3.4-1.6 1.4 c.8 1.8 2 3 3.6 3.8 l1.4-1.6 3.3 1.8-1 2.6 c-5.5.4-10.6-5-10-10.4z" fill="none" stroke="#3d3d3d" stroke-width="1.4" stroke-linejoin="round"/>
        </svg>
        <span>555-210-4830</span>
      </li>
      <li class="contact-item">
        <svg class="contact-icon" viewBox="0 0 28 28" aria-hidden="true">
          <circle cx="14" cy="14" r="12.5" fill="none" stroke="#3d3d3d" stroke-width="1.5"/>
          <rect x="7.5" y="9.5" width="13" height="9" fill="none" stroke="#3d3d3d" stroke-width="1.4"/>
          <path d="M7.5 9.5 l6.5 5 6.5-5 M7.5 18.5 l4.8-4.2 M20.5 18.5 l-4.8-4.2" fill="none" stroke="#3d3d3d" stroke-width="1.2"/>
        </svg>
        <span>care@halvornvision.com</span>
      </li>
      <li class="contact-item">
        <svg class="contact-icon" viewBox="0 0 28 28" aria-hidden="true">
          <circle cx="14" cy="14" r="12.5" fill="none" stroke="#3d3d3d" stroke-width="1.5"/>
          <circle cx="14" cy="14" r="8" fill="none" stroke="#3d3d3d" stroke-width="1.2"/>
          <ellipse cx="14" cy="14" rx="3.6" ry="8" fill="none" stroke="#3d3d3d" stroke-width="1.2"/>
          <path d="M6 14h16 M7.2 10h13.6 M7.2 18h13.6" stroke="#3d3d3d" stroke-width="1.1"/>
        </svg>
        <span>www.halvornvision.com</span>
      </li>
    </ul>
    <div class="address">48 Orchard Ridge Road, Marlow, MO, 64000</div>
  </section>

  <section class="card card--back">
    <div class="brand-mark"></div>
    <div class="brand-block">
      <div class="brand-name">Halvorn Vision<span class="brand-name__sub">Center</span></div>
      <p class="slogan">Neighborly Service, Expert Eye Care</p>
    </div>
  </section>
</body>
</html>
```